Halvercott Orthodontics business card

Using our existing logo (created with ArtFolio), please create a tasteful, contemporary business card. We are father and daughter orthodontists specializing in braces, clarafit, etc to design healthy, beautiful smiles for children, adolescents, and adults. We would like the design to be family-friendly but not childish.
The final design should include all of the information without looking cluttered (I hope! If necessary to achieve an optimal design, please consider making the card double-sided)
Purple, black, silver on a white card
Please include the following information:
Halvercott Orthodontics (logo)
Marguerite L. Halvercott, DMD
Douglas R. Halvercott, DMD

312 Bramblewood Street
North Andover, MA 01899
978.555.0142

847C Quarry Hollow Street
Methuen, MA 01898
978.555.0187

email frontdesk@halvercottortho.example
website www.halvercottortho.example

```html
<!DOCTYPE html>
<html lang="en">
<head>
<meta charset="utf-8">
<title>Halvercott Orthodontics business card</title>
<link rel="stylesheet" href="https://fonts.googleapis.com/css2?family=Figtree:wght@400;600;700&display=swap">
<style>
  :root {
    --purple: #5a2586;
    --purple-light: #6a2f98;
    --purple-dark: #4c1f73;
    --white: #ffffff;
    --paper: #f1f1f2;
    --backdrop: #e4e6e5;
    --text-on-purple: #f3eef8;
  }
  * { margin: 0; padding: 0; box-sizing: border-box; }
  html, body {
    width: 1200px; height: 1200px; overflow: hidden;
    background: var(--backdrop);
    font-family: "Figtree", Arial, sans-serif;
  }
  .card {
    position: absolute; left: 236px; width: 728px; height: 416px;
    border-radius: 4px; overflow: hidden;
    box-shadow: 0 6px 18px rgba(0,0,0,0.18);
  }
  .card-front { top: 134px; background: linear-gradient(180deg, var(--white), var(--paper)); }
  .card-back { top: 610px; }

  .brand {
    position: absolute; left: 0; right: 0; top: 0; height: 180px;
    display: flex; align-items: center; justify-content: center; gap: 14px;
  }
  .brand-dot { width: 26px; height: 26px; border-radius: 50%; background: var(--purple); }
  .brand-name {
    font-weight: 600; font-size: 34px; letter-spacing: 1px;
    color: var(--purple); text-transform: uppercase;
  }

  .office {
    position: absolute; top: 180px; height: 181px;
    background: linear-gradient(135deg, var(--purple-dark), var(--purple-light));
    color: var(--text-on-purple); text-align: center;
    padding-top: 17px;
  }
  .office-left { left: 0; width: 360px; }
  .office-right { left: 369px; width: 359px; }
  .doctor { font-weight: 700; font-size: 20px; line-height: 26px; }
  .phone { font-size: 18px; line-height: 24px; margin-top: 8px; display: flex; justify-content: center; align-items: center; gap: 8px; }
  .phone svg { width: 15px; height: 15px; }
  .office-name { font-weight: 700; font-size: 18px; line-height: 24px; margin-top: 8px; }
  .address { font-size: 18px; line-height: 27px; }

  .contact-band {
    position: absolute; left: 0; right: 0; top: 371px; height: 45px;
    background: linear-gradient(90deg, var(--purple-dark), var(--purple-light));
    color: var(--text-on-purple); font-size: 18px;
    display: flex; align-items: center; justify-content: space-around; padding: 0 14px;
  }
  .contact-item { display: flex; align-items: center; gap: 10px; }
  .contact-item svg { width: 16px; height: 16px; }

  .back-field {
    position: absolute; inset: 0;
    background: linear-gradient(135deg, var(--purple-dark), var(--purple-light));
  }
  .back-brand {
    position: absolute; left: 326px; top: 262px;
    display: flex; align-items: center; gap: 12px;
  }
  .back-brand .brand-dot { background: var(--white); width: 22px; height: 22px; }
  .back-brand .brand-name { color: var(--white); font-size: 22px; }
</style>
</head>
<body>
  <section class="card card-front">
    <div class="brand">
      <span class="brand-dot"></span>
      <span class="brand-name">Halvercott Orthodontics</span>
    </div>

    <div class="office office-left">
      <p class="doctor">Marguerite L. Halvercott, DMD</p>
      <p class="phone">
        <svg viewBox="0 0 24 24" fill="currentColor"><path d="M6.6 10.8a15 15 0 0 0 6.6 6.6l2.2-2.2a1 1 0 0 1 1-.25 11.4 11.4 0 0 0 3.6.57 1 1 0 0 1 1 1V20a1 1 0 0 1-1 1A17 17 0 0 1 3 4a1 1 0 0 1 1-1h3.5a1 1 0 0 1 1 1c0 1.25.2 2.45.57 3.57a1 1 0 0 1-.25 1z"/></svg>
        978-555-0142
      </p>
      <p class="office-name">North Andover Office</p>
      <p class="address">312 Bramblewood St.<br>North Andover, MA 01899</p>
    </div>

    <div class="office office-right">
      <p class="doctor">Douglas R. Halvercott, DMD</p>
      <p class="phone">
        <svg viewBox="0 0 24 24" fill="currentColor"><path d="M6.6 10.8a15 15 0 0 0 6.6 6.6l2.2-2.2a1 1 0 0 1 1-.25 11.4 11.4 0 0 0 3.6.57 1 1 0 0 1 1 1V20a1 1 0 0 1-1 1A17 17 0 0 1 3 4a1 1 0 0 1 1-1h3.5a1 1 0 0 1 1 1c0 1.25.2 2.45.57 3.57a1 1 0 0 1-.25 1z"/></svg>
        978-555-0187
      </p>
      <p class="office-name">Methuen Office</p>
      <p class="address">847C Quarry Hollow St.<br>Methuen, MA 01898</p>
    </div>

    <div class="contact-band">
      <span class="contact-item">
        <svg viewBox="0 0 24 24" fill="currentColor"><path d="M2 5h20v14H2z M2 5l10 8 10-8" stroke="#5a2586" stroke-width="1.6"/></svg>
        frontdesk@halvercottortho.example
      </span>
      <span class="contact-item">
        <svg viewBox="0 0 24 24" fill="none" stroke="currentColor" stroke-width="2"><circle cx="12" cy="12" r="9"/><path d="M3 12h18M12 3c3 3 3 15 0 18M12 3c-3 3-3 15 0 18"/></svg>
        www.halvercottortho.example
      </span>
    </div>
  </section>

  <section class="card card-back">
    <div class="back-field" role="img" aria-label="Purple card back with a faint embossed repeat of the practice symbol"></div>
    <div class="back-brand">
      <span class="brand-dot"></span>
      <span class="brand-name">Halvercott Orthodontics</span>
    </div>
  </section>
</body>
</html>
```